Business Consulting Company needs a business card designed

We need a business card in Brisbane Australia for a company called " Marrowvale Consulting Group". I would like to see the designs either in purple or green color

```html
<!DOCTYPE html>
<html lang="en">
<head>
<meta charset="utf-8">
<title>Marrowvale Consulting Group – Business Card</title>
<link rel="stylesheet" href="https://fonts.googleapis.com/css2?family=Didact+Gothic&family=Open+Sans:wght@400;600;700&display=swap">
<style>
  :root {
    --bg: #e9e6e1;
    --green-dark: #0b6b35;
    --green: #129448;
    --green-light: #3dbb6c;
    --green-accent: #1a9b4e;
    --silver: #e4e6e5;
    --ink: #1c1c1c;
    --paper: #ffffff;
    --faint: #eef4f0;
  }
  * { box-sizing: border-box; margin: 0; padding: 0; }
  html, body { width: 1200px; height: 784px; overflow: hidden; }
  body {
    background: var(--bg);
    position: relative;
    font-family: "Open Sans", Arial, sans-serif;
  }
  .card {
    position: absolute;
    top: 237px;
    width: 540px;
    height: 309px;
    border-radius: 4px;
    box-shadow: 0 6px 18px rgba(0,0,0,.18);
    overflow: hidden;
  }
  /* Front */
  .card-front { left: 40px; background: var(--green); }
  .front-pattern {
    position: absolute; inset: 0;
    background:
      radial-gradient(ellipse at 25% 80%, rgba(90,200,120,.45), transparent 60%),
      radial-gradient(ellipse at 80% 15%, rgba(5,70,35,.6), transparent 60%),
      linear-gradient(135deg, var(--green-light) 0%, var(--green) 50%, var(--green-dark) 100%);
  }
  .front-brand {
    position: absolute; left: 0; right: 0; top: 70px;
    display: flex; flex-direction: column; align-items: center; gap: 22px;
  }
  .front-mark {
    width: 92px; height: 92px; border-radius: 50%;
    background: var(--silver);
  }
  .front-name {
    font-family: "Didact Gothic", "Century Gothic", sans-serif;
    font-size: 30px; color: var(--silver); letter-spacing: .3px;
  }
  /* Back */
  .card-back { left: 620px; background: var(--paper); }
  .back-deco {
    position: absolute; right: -40px; top: 70px;
    width: 230px; height: 230px; border-radius: 50%;
    background: var(--faint);
  }
  .back-brand {
    position: absolute; left: 38px; top: 58px;
    display: flex; align-items: center; gap: 14px;
  }
  .back-mark {
    width: 78px; height: 78px; border-radius: 50%;
    background: var(--green-accent);
  }
  .back-name {
    font-family: "Didact Gothic", "Century Gothic", sans-serif;
    font-size: 25px; color: var(--ink);
  }
  .person {
    position: absolute; left: 42px; top: 168px;
  }
  .person-name { font-size: 19px; font-weight: 700; color: var(--green-accent); line-height: 1.1; }
  .person-role { font-size: 12px; color: var(--ink); margin-top: 2px; }
  .contacts {
    list-style: none; position: absolute; left: 42px; top: 218px;
    font-size: 13px; color: var(--ink); line-height: 1.45;
  }
  .contacts li { display: flex; align-items: flex-start; gap: 7px; }
  .contacts svg { width: 13px; height: 13px; margin-top: 3px; flex: none; fill: var(--green-accent); }
</style>
</head>
<body>
  <section class="card card-front">
    <div class="front-pattern" role="img" aria-label="Green background with a receding pattern of soft oval dots"></div>
    <div class="front-brand">
      <div class="front-mark"></div>
      <div class="front-name">Marrowvale Consulting Group</div>
    </div>
  </section>

  <section class="card card-back">
    <div class="back-deco"></div>
    <div class="back-brand">
      <div class="back-mark"></div>
      <div class="back-name">Marrowvale Consulting Group</div>
    </div>
    <div class="person">
      <div class="person-name">Dana Whitlock</div>
      <div class="person-role">manager</div>
    </div>
    <ul class="contacts">
      <li>
        <svg viewBox="0 0 16 16" aria-hidden="true"><path d="M3.5 1l3 3-1.5 2c1 2 3 4 5 5l2-1.5 3 3-2 2.5C7 14 2 9 1 3.5z"/></svg>
        <span>154-730-2916</span>
      </li>
      <li>
        <svg viewBox="0 0 16 16" aria-hidden="true"><circle cx="8" cy="8" r="7"/><path d="M1 8h14M8 1v14" stroke="#fff" stroke-width="1.2"/><ellipse cx="8" cy="8" rx="3" ry="7" fill="none" stroke="#fff" stroke-width="1.2"/></svg>
        <span>www.marrowvaleconsulting.com</span>
      </li>
      <li>
        <svg viewBox="0 0 16 16" aria-hidden="true"><rect x="1" y="3" width="14" height="10" rx="1"/><path d="M1.5 3.5L8 9l6.5-5.5" fill="none" stroke="#fff" stroke-width="1.3"/></svg>
        <span>info@marrowvaleconsulting.com</span>
      </li>
      <li>
        <svg viewBox="0 0 16 16" aria-hidden="true"><path d="M8 1L1 7.5h2V15h4v-4h2v4h4V7.5h2z"/></svg>
        <span>27 Kestrel Lane, Hollis Bay,<br>MA 02190</span>
      </li>
    </ul>
  </section>
</body>
</html>
```